Brimvantel

We are re-branding the company with a new logo (attached) which I would
like to go on one side of the card, and I have attached a file showing what
the old back side looked like, and I do like the characters that show the
phone, e-mails, etc., I don't like the current arrangement, and I want
something clean, clear and out of the box, as we are an aviation consulting
firm, and we work outside of the box.

```html
<!DOCTYPE html>
<html lang="en">
<head>
<meta charset="utf-8">
<title>Brimvantel – Business Card</title>
<link rel="stylesheet" href="https://fonts.googleapis.com/css2?family=Open+Sans:wght@400;600;700&display=swap">
<style>
  :root {
    --canvas: #e4e6e6;
    --paper: #ffffff;
    --ink: #1f1f1f;
    --ink-soft: #8a8a8a;
    --brand-red: #b3191f;
    --panel-light: #4a4a4a;
    --panel-dark: #2c2c2c;
    --panel-text: #ffffff;
    --mark-grey: #c9c9c9;
  }
  * { box-sizing: border-box; margin: 0; padding: 0; }
  html, body { width: 1000px; height: 1200px; overflow: hidden; }
  body {
    position: relative;
    background: var(--canvas);
    font-family: "Open Sans", Arial, sans-serif;
    color: var(--ink);
  }
  .card {
    position: absolute;
    left: 146px;
    width: 683px;
    height: 399px;
    background: var(--paper);
    overflow: hidden;
  }
  .card--front { top: 117px; }
  .card--back  { top: 655px; }

  /* Brand lockup */
  .brand {
    position: absolute;
    left: 0;
    display: flex;
    flex-direction: column;
    align-items: center;
  }
  .brand__row { display: flex; align-items: center; gap: 14px; }
  .brand__dot { border-radius: 50%; background: var(--mark-grey); flex: none; }
  .brand__name {
    font-weight: 600;
    color: var(--ink);
    letter-spacing: 1px;
    line-height: 1;
  }
  .brand__tagline {
    color: var(--ink-soft);
    letter-spacing: 0.3px;
    white-space: nowrap;
  }
  .brand__tagline .sep { color: var(--brand-red); }

  .card--front .brand { top: 150px; width: 468px; }
  .card--front .brand__dot { width: 38px; height: 38px; }
  .card--front .brand__name { font-size: 44px; }
  .card--front .brand__tagline { font-size: 12px; margin-top: 6px; }

  .card--back .brand { top: 190px; width: 683px; }
  .card--back .brand__dot { width: 50px; height: 50px; }
  .card--back .brand__name { font-size: 56px; }
  .card--back .brand__tagline { font-size: 14.5px; margin-top: 8px; }

  /* Services */
  .services {
    position: absolute;
    left: 0;
    top: 282px;
    width: 468px;
    text-align: center;
    font-size: 15.5px;
    line-height: 24px;
    list-style: none;
  }
  .services li { display: inline; }
  .services .bullet {
    display: inline-block;
    width: 7px; height: 7px;
    background: var(--brand-red);
    margin: 0 8px 2px;
  }

  /* Contact panel */
  .contact-panel {
    position: absolute;
    left: 468px;
    top: 0;
    width: 215px;
    height: 399px;
    background: radial-gradient(ellipse at 55% 40%, var(--panel-light) 0%, var(--panel-dark) 80%);
    color: var(--panel-text);
  }
  .contact-panel__notch {
    position: absolute;
    left: 0;
    top: 50px;
    width: 0; height: 0;
    border-top: 10px solid transparent;
    border-bottom: 10px solid transparent;
    border-left: 12px solid var(--paper);
  }
  .person__name {
    position: absolute;
    left: 25px;
    top: 51px;
    font-size: 14px;
    letter-spacing: 0.4px;
    font-weight: 400;
    white-space: nowrap;
  }
  .person__name strong { font-weight: 700; }
  .person__role {
    position: absolute;
    left: 0;
    width: 200px;
    top: 80px;
    text-align: center;
    font-size: 10.5px;
  }
  .contact-list { list-style: none; }
  .contact-item {
    position: absolute;
    left: 24px;
    display: flex;
    align-items: flex-start;
    gap: 12px;
    font-size: 12.5px;
    line-height: 14px;
  }
  .contact-item__icon {
    width: 26px; height: 26px;
    background: var(--brand-red);
    display: flex; align-items: center; justify-content: center;
    flex: none;
  }
  .contact-item--address { top: 243px; }
  .contact-item--phone   { top: 288px; }
  .contact-item--web     { top: 335px; }
</style>
</head>
<body>

<section class="card card--front" aria-label="Business card front">
  <div class="brand">
    <div class="brand__row">
      <span class="brand__dot"></span>
      <span class="brand__name">Brimvantel</span>
    </div>
    <p class="brand__tagline">steady guidance <span class="sep">•</span> reliable outcomes</p>
  </div>

  <ul class="services">
    <li><span class="bullet"></span>Aircraft Finance/ Leasing</li>
    <li><span class="bullet"></span>Technical services<span class="bullet"></span></li><br>
    <li><span class="bullet"></span>Aviation consulting</li>
    <li><span class="bullet"></span>Airline restructuring<span class="bullet"></span></li>
  </ul>

  <aside class="contact-panel">
    <span class="contact-panel__notch"></span>
    <h2 class="person__name">DORIAN K. <strong>HALVORSEN</strong></h2>
    <p class="person__role">President &amp; CEO</p>

    <ul class="contact-list">
      <li class="contact-item contact-item--address">
        <span class="contact-item__icon">
          <svg width="14" height="14" viewBox="0 0 14 14"><path d="M7 1.5 L13 7 H11 V12.5 H8.3 V9 H5.7 V12.5 H3 V7 H1 Z" fill="#fff"/></svg>
        </span>
        <span>2740B Maple Ridge<br>Lindell, CA 94318</span>
      </li>
      <li class="contact-item contact-item--phone">
        <span class="contact-item__icon">
          <svg width="14" height="14" viewBox="0 0 14 14"><path d="M3.2 1.2 L5.3 3.6 L4.2 5.2 C5 7 6.6 8.7 8.6 9.6 L10.2 8.5 L12.7 10.6 L11.4 12.6 C6.4 12.4 1.5 7.6 1.2 2.6 Z" fill="#fff"/></svg>
        </span>
        <span>+1 555 201 4736<br>+1 555 388 0914</span>
      </li>
      <li class="contact-item contact-item--web">
        <span class="contact-item__icon">
          <svg width="14" height="14" viewBox="0 0 14 14" fill="none" stroke="#fff" stroke-width="1.2"><circle cx="7" cy="7" r="5.6"/><ellipse cx="7" cy="7" rx="2.4" ry="5.6"/><line x1="1.4" y1="7" x2="12.6" y2="7"/><line x1="2.2" y1="4.2" x2="11.8" y2="4.2"/><line x1="2.2" y1="9.8" x2="11.8" y2="9.8"/></svg>
        </span>
        <span>dh@brv.aero<br>www.brv.aero</span>
      </li>
    </ul>
  </aside>
</section>

<section class="card card--back" aria-label="Business card back">
  <div class="brand">
    <div class="brand__row">
      <span class="brand__dot"></span>
      <span class="brand__name">Brimvantel</span>
    </div>
    <p class="brand__tagline">steady guidance <span class="sep">•</span> reliable outcomes</p>
  </div>
</section>

</body>
</html>
```